Careway Transit private ambulance flyer/broshure

I need a Tri-fold brochure for our BLS non-emergency private ambulance company. We transport patients to doctors appointments, hyperbarics, dialysis, out of town doctors appointment and scheduled medical procedures etc.

```html
<!DOCTYPE html>
<html lang="en">
<head>
<meta charset="utf-8">
<title>Careway Transit – Tri-fold Brochure</title>
<link rel="stylesheet" href="https://fonts.googleapis.com/css2?family=Montserrat:wght@500;600;700;800&family=Poppins:wght@400;500&display=swap">
<style>
  :root{
    --bg:#eeeef8;
    --paper:#f4f4f6;
    --grey:#d9dadd;
    --blue:#3b33a0;
    --blue-deep:#2c2685;
    --green:#5db531;
    --green-dark:#3f9a23;
    --ink:#222;
    --white:#fff;
  }
  *{box-sizing:border-box;margin:0;padding:0}
  html,body{width:933px;height:1200px;overflow:hidden;background:var(--bg)}
  body{position:relative;font-family:"Poppins",sans-serif;color:var(--ink)}
  .sprite{position:absolute;width:0;height:0}
  .side{position:absolute;left:26px;width:880px;height:555px;background:linear-gradient(180deg,#fbfbfc,var(--paper));overflow:hidden;box-shadow:0 6px 18px rgba(40,40,90,.18)}
  .side--outside{top:22px}
  .side--inside{top:622px}
  .deco{position:absolute;inset:0}
  .fold{position:absolute;top:0;bottom:0;width:1px;background:rgba(0,0,0,.06)}
  .pill{position:absolute;background:linear-gradient(180deg,var(--green),var(--green-dark));color:var(--white);font-family:"Montserrat",sans-serif;font-weight:700;font-size:15px;padding:6px 18px;border-radius:18px;letter-spacing:.3px}
  .body-text{position:absolute;font-size:9.2px;line-height:1.38;text-align:justify}
  .body-text p+p{margin-top:9px}
  .body-text .lead::before{content:"›";color:var(--blue);font-weight:700;margin-right:5px}
  .photo{position:absolute}
  .phone-band{position:absolute;color:var(--white);font-size:15px;font-weight:500;letter-spacing:.5px;text-align:center;width:293px}
  .brand{position:absolute;display:flex;align-items:center;gap:8px;font-family:"Montserrat",sans-serif;font-weight:800;color:var(--blue)}
  .brand__dot{width:18px;height:18px;border-radius:50%;background:var(--green)}
  .contact{position:absolute;display:flex;align-items:center;gap:6px;color:var(--white)}
  .contact svg{width:22px;height:22px;flex:none}
  .contact__label{font-family:"Montserrat",sans-serif;font-weight:700;font-size:13px;line-height:1}
  .contact__num{font-size:9.5px;color:#a9e486;line-height:1.2}
  .contact__addr{font-size:8px;line-height:1.3}
  .panel-blue-text{position:absolute;color:var(--white);font-family:"Montserrat",sans-serif;font-weight:600;text-align:center}
  .cover-title{position:absolute;left:587px;width:293px;text-align:center;font-family:"Montserrat",sans-serif;font-weight:800;line-height:1.05}
  .services{position:absolute;left:310px;top:198px;width:262px;list-style:none}
  .services li{display:flex;align-items:center;gap:12px;color:var(--white);font-family:"Montserrat",sans-serif;font-weight:600;font-size:9px;line-height:1.3;padding:6px 0;min-height:42px;border-bottom:1px solid rgba(255,255,255,.25)}
  .services li:last-child{border-bottom:none}
  .services svg{width:30px;height:30px;flex:none}
</style>
</head>
<body>

<svg class="sprite" aria-hidden="true">
  <symbol id="icon-phone" viewBox="0 0 24 24">
    <circle cx="12" cy="12" r="12" fill="#5db531"/>
    <path d="M8.3 6.2l1.8-.4 1.2 2.8-1.2 1a7 7 0 0 0 3.6 3.6l1-1.2 2.8 1.2-.4 1.8c-.2.6-.8 1-1.4.9A10 10 0 0 1 7.4 7.6c-.1-.6.3-1.2.9-1.4z" fill="#fff"/>
  </symbol>
</svg>

<!-- OUTSIDE SPREAD -->
<section class="side side--outside" aria-label="Brochure outside">
  <svg class="deco" viewBox="0 0 880 555" aria-hidden="true">
    <path d="M0 0H880V60C620 40 330 120 0 150Z" fill="#dcdde0"/>
    <path d="M0 150C330 120 620 40 880 60" fill="none" stroke="#5db531" stroke-width="6"/>
    <path d="M0 160C330 130 620 50 880 70" fill="none" stroke="#3b33a0" stroke-width="2"/>
    <path d="M293 85C400 70 500 55 587 45V420C500 440 400 450 293 445Z" fill="#3b33a0"/>
    <path d="M293 445C400 450 500 440 587 420" fill="none" stroke="#5db531" stroke-width="4"/>
    <path d="M0 525C260 515 560 495 880 460V555H0Z" fill="#5db531"/>
    <path d="M0 520C260 510 560 490 880 455" fill="none" stroke="#3b33a0" stroke-width="3"/>
  </svg>
  <div class="fold" style="left:293px"></div>
  <div class="fold" style="left:587px"></div>

  <!-- left panel -->
  <div class="pill" style="left:28px;top:166px">WHO WE ARE</div>
  <div class="body-text" style="left:24px;top:202px;width:250px">
    <p class="lead">Careway Transit is a trusted provider of exceptional healthcare transportation services, dedicated to ensuring that individuals in our community have access to reliable and compassionate transportation solutions. With years of experience in the industry, we have earned a reputation for excellence in delivering safe, punctual, and personalized transportation to medical appointments, treatments, and specialized care facilities.</p>
    <p>At Careway Transit, we understand the importance of each journey, and we are committed to providing the highest level of care to our passengers. Our team of professional drivers and support staff is dedicated to ensuring that every trip is comfortable, stress-free, and tailored to the unique needs of our clients.</p>
  </div>
  <svg class="photo" style="left:20px;top:430px" width="140" height="125" viewBox="0 0 140 125" role="img" aria-label="Photo of a row of parked ambulances">
    <defs><linearGradient id="g-fleet" x1="0" x2="1"><stop offset="0" stop-color="#c9ccd2"/><stop offset=".6" stop-color="#e9e2e0"/><stop offset="1" stop-color="#b9bec8"/></linearGradient></defs>
    <circle cx="70" cy="70" r="66" fill="url(#g-fleet)" stroke="#3b33a0" stroke-width="6"/>
  </svg>

  <!-- middle panel -->
  <svg class="photo" style="left:370px;top:62px" width="140" height="140" viewBox="0 0 140 140" role="img" aria-label="Street map showing the office location">
    <circle cx="70" cy="70" r="66" fill="#eef0f3" stroke="#fff" stroke-width="6"/>
  </svg>
  <div class="panel-blue-text" style="left:305px;top:218px;width:270px;font-size:10.5px;line-height:1.35">FOR MORE INFORMATION ABOUT<br>CAREWAY TRANSIT, PLEASE<br>CONTACT US.</div>
  <div class="pill" style="left:370px;top:270px">GET IN TOUCH</div>
  <div class="contact" style="left:318px;top:318px"><svg><use href="#icon-phone"/></svg><div><div class="contact__label">OFFICE</div><div class="contact__num">210-555-0148</div></div></div>
  <div class="contact" style="left:450px;top:318px"><svg><use href="#icon-phone"/></svg><div><div class="contact__label">FAX</div><div class="contact__num">210-555-0131</div></div></div>
  <div class="contact" style="left:380px;top:356px"><svg><use href="#icon-phone"/></svg><div><div class="contact__label">AFTER HOURS</div><div class="contact__num">210-555-0150</div></div></div>
  <div class="contact" style="left:380px;top:394px">
    <svg viewBox="0 0 24 24"><circle cx="12" cy="12" r="11" fill="#fff"/><path d="M6 12l6-5 6 5v6h-4v-4h-4v4H6z" fill="#3b33a0"/></svg>
    <div class="contact__addr">1180 Cedar Bend Rd, Riverton,<br>TX 78000, United States</div>
  </div>
  <div class="brand" style="left:370px;top:462px;font-size:17px"><span class="brand__dot"></span>Careway Transit</div>
  <div class="phone-band" style="left:293px;top:518px">210-555-0150</div>

  <!-- right cover -->
  <div class="brand" style="left:640px;top:92px;font-size:20px"><span class="brand__dot"></span>Careway Transit</div>
  <div class="cover-title" style="top:130px;color:var(--blue);font-size:19px">NON-EMERGENCY</div>
  <div class="cover-title" style="top:152px;color:var(--ink);font-size:12px;font-weight:700">PRIVATE AMBULANCE<br>SERVICES</div>
  <svg class="photo" style="left:587px;top:190px" width="293" height="200" viewBox="0 0 293 200" role="img" aria-label="Photo of an ambulance driving with lights on">
    <defs><linearGradient id="g-amb" x1="0" y1="0" x2="1" y2="1"><stop offset="0" stop-color="#c8c4c4"/><stop offset=".5" stop-color="#eeeeee"/><stop offset="1" stop-color="#9a7d78"/></linearGradient></defs>
    <path d="M0 0H293V100C200 140 100 170 0 185Z" fill="url(#g-amb)"/>
    <path d="M0 185C100 170 200 140 293 100" fill="none" stroke="#3b33a0" stroke-width="5"/>
    <path d="M0 193C100 178 200 148 293 108" fill="none" stroke="#5db531" stroke-width="4"/>
  </svg>
  <div class="cover-title" style="top:405px;color:var(--blue);font-size:26px">BLS &amp; ACLS</div>
  <div class="pill" style="left:612px;top:440px;font-size:11.5px;padding:5px 16px">TRANSFERS &amp; DISCHARGES</div>
  <div class="phone-band" style="left:587px;top:512px">210-555-0148</div>
</section>

<!-- INSIDE SPREAD -->
<section class="side side--inside" aria-label="Brochure inside">
  <svg class="deco" viewBox="0 0 880 555" aria-hidden="true">
    <rect x="293" y="0" width="294" height="555" fill="#3b33a0"/>
    <path d="M0 0H293V30C200 40 100 60 0 80Z" fill="#dcdde0"/>
    <path d="M0 80C100 60 200 40 293 30" fill="none" stroke="#5db531" stroke-width="5"/>
    <path d="M0 525C260 515 560 495 880 460V555H0Z" fill="#5db531"/>
    <path d="M0 520C260 510 560 490 880 455" fill="none" stroke="#3b33a0" stroke-width="3"/>
  </svg>
  <div class="fold" style="left:293px"></div>
  <div class="fold" style="left:587px"></div>

  <!-- left panel -->
  <div class="pill" style="left:28px;top:70px">ABOUT US</div>
  <div class="body-text" style="left:24px;top:108px;width:250px">
    <p class="lead">At Careway Transit, we are dedicated to providing exceptional healthcare transportation solutions tailored to meet the diverse needs of our clients. With a team of highly trained professionals and a fleet of modern vehicles, we ensure safe, reliable, and comfortable transportation to medical appointments, treatments, and procedures. Our mission is to bridge the gap in access to essential healthcare services, enabling individuals to receive the care they need promptly and conveniently. Whether it's assisting elderly individuals, individuals with disabilities, or those requiring specialized medical care, we are committed to delivering compassionate and personalized service every step of the way. With Careway Transit, you can trust that your healthcare transportation needs are in capable hands.</p>
  </div>
  <svg class="photo" style="left:20px;top:376px" width="273" height="132" viewBox="0 0 273 132" role="img" aria-label="Photo of nurses caring for a patient on a hospital bed">
    <defs><linearGradient id="g-nurses" x1="0" x2="1"><stop offset="0" stop-color="#8fb6d6"/><stop offset=".5" stop-color="#e9eef3"/><stop offset="1" stop-color="#7aa6c9"/></linearGradient></defs>
    <path d="M0 60C80 20 180 0 273 0V128C180 130 80 131 0 132Z" fill="url(#g-nurses)"/>
    <path d="M0 60C80 20 180 0 273 0" fill="none" stroke="#5db531" stroke-width="5"/>
  </svg>
  <svg class="photo" style="left:150px;top:316px" width="120" height="120" viewBox="0 0 120 120" role="img" aria-label="Photo of paramedics moving a patient on a stretcher">
    <defs><linearGradient id="g-stretcher" x1="0" x2="1" y1="0" y2="1"><stop offset="0" stop-color="#6d7ca6"/><stop offset="1" stop-color="#c9d3e8"/></linearGradient></defs>
    <circle cx="60" cy="60" r="55" fill="url(#g-stretcher)" stroke="#9ed57f" stroke-width="8"/>
  </svg>
  <div class="phone-band" style="left:0;top:522px">210-555-0148</div>

  <!-- middle panel -->
  <svg class="photo" style="left:375px;top:20px" width="130" height="130" viewBox="0 0 130 130" role="img" aria-label="Photo of a paramedic with a smiling patient on a stretcher">
    <defs><linearGradient id="g-patient" x1="0" x2="1"><stop offset="0" stop-color="#3a3a52"/><stop offset=".6" stop-color="#d7ccc6"/><stop offset="1" stop-color="#e9e9ee"/></linearGradient></defs>
    <circle cx="65" cy="65" r="61" fill="url(#g-patient)" stroke="#5a52b8" stroke-width="6"/>
  </svg>
  <div class="pill" style="left:330px;top:158px">SERVICES WE PROVIDE</div>
  <ul class="services">
    <li><svg viewBox="0 0 30 30"><circle cx="15" cy="15" r="15" fill="#5db531"/><rect x="7" y="11" width="12" height="8" fill="#fff"/><path d="M19 13h3l2 3v3h-5z" fill="#fff"/><circle cx="11" cy="20" r="2" fill="#3f9a23"/><circle cx="21" cy="20" r="2" fill="#3f9a23"/></svg><span>BLS NON-EMERGENCY<br>PRIVATE AMBULANCE SERVICES,</span></li>
    <li><svg viewBox="0 0 30 30"><circle cx="15" cy="15" r="15" fill="#5db531"/><path d="M13 8h4v5h5v4h-5v5h-4v-5H8v-4h5z" fill="#fff"/></svg><span>TRANSPORTATION FOR PATIENTS TO DOCTOR'S APPOINTMENTS, HYPERBARIC TREATMENTS, DIALYSIS</span></li>
    <li><svg viewBox="0 0 30 30"><circle cx="15" cy="15" r="15" fill="#5db531"/><path d="M15 7a5 5 0 0 1 5 5c0 4-5 10-5 10s-5-6-5-10a5 5 0 0 1 5-5z" fill="#fff"/><circle cx="15" cy="12" r="2" fill="#3f9a23"/></svg><span>OUT-OF-TOWN DOCTOR'S<br>APPOINTMENTS,</span></li>
    <li><svg viewBox="0 0 30 30"><circle cx="15" cy="15" r="15" fill="#5db531"/><path d="M15 22l-6-6a3.5 3.5 0 0 1 6-4 3.5 3.5 0 0 1 6 4z" fill="#fff"/></svg><span>SCHEDULED MEDICAL<br>PROCEDURES.</span></li>
  </ul>
  <div class="panel-blue-text" style="left:310px;top:396px;color:#8fd65f;font-size:14px;font-weight:700">GET IN TOUCH</div>
  <div class="contact" style="left:318px;top:420px"><svg><use href="#icon-phone"/></svg><div><div class="contact__label">OFFICE</div><div class="contact__num">210-555-0148</div></div></div>
  <div class="contact" style="left:450px;top:420px"><svg><use href="#icon-phone"/></svg><div><div class="contact__label">FAX</div><div class="contact__num">210-555-0131</div></div></div>
  <div class="contact" style="left:380px;top:456px"><svg><use href="#icon-phone"/></svg><div><div class="contact__label">AFTER HOURS</div><div class="contact__num">210-555-0150</div></div></div>
  <div class="phone-band" style="left:293px;top:514px">210-555-0150</div>

  <!-- right panel -->
  <svg class="photo" style="left:587px;top:0" width="293" height="215" viewBox="0 0 293 215" role="img" aria-label="Photo of paramedics treating a patient with an oxygen mask">
    <defs><linearGradient id="g-treat" x1="0" x2="1" y1="0" y2="1"><stop offset="0" stop-color="#d8d2cc"/><stop offset=".5" stop-color="#e9c8b8"/><stop offset="1" stop-color="#c96a50"/></linearGradient></defs>
    <path d="M0 0H293V60C230 150 120 190 0 205Z" fill="url(#g-treat)"/>
    <path d="M0 205C120 190 230 150 293 60" fill="none" stroke="#5db531" stroke-width="6"/>
  </svg>
  <svg class="photo" style="left:740px;top:95px" width="125" height="125" viewBox="0 0 125 125" role="img" aria-label="Photo of a paramedic beside a stretcher outdoors">
    <defs><linearGradient id="g-medic" x1="0" x2="1"><stop offset="0" stop-color="#b84a36"/><stop offset="1" stop-color="#dde3e6"/></linearGradient></defs>
    <circle cx="62.5" cy="62.5" r="57" fill="url(#g-medic)" stroke="#9ed57f" stroke-width="8"/>
  </svg>
  <div class="pill" style="left:610px;top:252px">WHY CHOOSE US</div>
  <div class="body-text" style="left:607px;top:292px;width:250px">
    <p class="lead">Careway Transit is dedicated to offering comprehensive and compassionate healthcare transportation solutions, tailored to meet the diverse needs of our clients, including elderly individuals, individuals with disabilities, and those requiring specialized medical care, thereby bridging the gap in access to vital healthcare services by providing safe, reliable, and punctual transportation to medical appointments, treatments, and procedures, ultimately contributing to improved health outcomes and quality of life for our clients and their families.</p>
  </div>
  <div class="phone-band" style="left:587px;top:485px">210-555-0148</div>
</section>

</body>
</html>
```